Business Card + Stationery Design for a Craft Beer Bar

Mr. Tovell's is a taproom sport bar that contains in its menu beers from different places around the world. What we offer differently is the experience that you can get inside our location, ambient music with rock from the 80s to 90s, projection with the sports of the moment, board games and private events.

Target Market(s)

Young people, Mid and High Class

Industry/Entity Type

Business

Font styles to use
Serif
Sans Serif

Colors
fee18a

Requirements
Must have
• Name, Title, Contact Details, Website
Nice to have
• Mail Signature
Should not have
• n/a

```html
<!DOCTYPE html>
<html lang="en">
<head>
<meta charset="utf-8">
<title>Mr. Tovell's Taproom – Business Card</title>
<link rel="stylesheet" href="https://fonts.googleapis.com/css2?family=Open+Sans:wght@400;600;700&display=swap">
<style>
  :root {
    --page-bg: #3b3532;
    --card-black: #070707;
    --card-grey: #1e1e1e;
    --accent-yellow: #fcc451;
    --text-white: #ffffff;
    --tab-silver: #d9d9d9;
  }
  * { box-sizing: border-box; margin: 0; padding: 0; }
  html, body { width: 1200px; height: 844px; overflow: hidden; }
  body {
    background: var(--page-bg);
    font-family: "Open Sans", Arial, sans-serif;
    position: relative;
  }
  .card {
    position: absolute;
    top: 279px;
    width: 500px;
    height: 286px;
    overflow: hidden;
    box-shadow: 0 10px 24px rgba(0, 0, 0, 0.45);
  }
  /* Contact side */
  .card--contact {
    left: 70px;
    background: linear-gradient(100deg, var(--card-black) 55%, var(--card-grey) 100%);
    border-top: 13px solid var(--accent-yellow);
    border-bottom: 13px solid var(--accent-yellow);
    color: var(--text-white);
    text-align: center;
  }
  .contact-person {
    margin: 40px auto 0;
    display: inline-block;
  }
  .contact-person__name {
    color: var(--accent-yellow);
    font-weight: 700;
    font-size: 16px;
    letter-spacing: 0.2px;
    padding-bottom: 2px;
    border-bottom: 1px solid var(--accent-yellow);
  }
  .contact-person__title {
    font-size: 13px;
    margin-top: 2px;
  }
  .contact-details {
    margin-top: 34px;
    font-size: 13px;
    line-height: 1.45;
  }
  .contact-address {
    margin-top: 30px;
    font-size: 13px;
  }
  /* Brand side */
  .card--brand {
    left: 630px;
    background: radial-gradient(ellipse at 50% 40%, #2a2a2a 0%, var(--card-black) 70%);
  }
  .brand-tab {
    position: absolute;
    width: 26px;
    height: 42px;
    background: var(--accent-yellow);
  }
  .brand-tab::before {
    content: "";
    position: absolute;
    top: 0;
    width: 4px;
    height: 100%;
    background: var(--tab-silver);
  }
  .brand-tab--top { right: 0; top: 42px; }
  .brand-tab--top::before { left: -4px; }
  .brand-tab--side { left: 0; top: 150px; }
  .brand-tab--side::before { right: -4px; }
  .brand-name {
    position: absolute;
    left: 0; right: 0;
    top: 0; bottom: 0;
    display: flex;
    align-items: center;
    justify-content: center;
    gap: 12px;
  }
  .brand-name__dot {
    width: 14px;
    height: 14px;
    border-radius: 50%;
    background: var(--accent-yellow);
  }
  .brand-name__text {
    color: var(--text-white);
    font-weight: 400;
    font-size: 28px;
    letter-spacing: 0.3px;
  }
</style>
</head>
<body>
  <section class="card card--contact">
    <div class="contact-person">
      <p class="contact-person__name">MARCUS ELLERY</p>
      <p class="contact-person__title">Managing Director</p>
    </div>
    <div class="contact-details">
      <p>044-218-5073</p>
      <p>hello@tovellstaproom.com</p>
      <p>www.tovellstaproom.com</p>
    </div>
    <p class="contact-address">58 Harbour Lane | Calder Bay, AB | 204817</p>
  </section>

  <section class="card card--brand">
    <span class="brand-tab brand-tab--top"></span>
    <span class="brand-tab brand-tab--side"></span>
    <div class="brand-name">
      <span class="brand-name__dot"></span>
      <p class="brand-name__text">Mr. Tovell's</p>
    </div>
  </section>
</body>
</html>
```